Gordon Pellbrook Consulting - Web Design Project

We need a web design for my new edgy consulting business specializing in innovation, technology and strategy.

It is our personal goal to turn each client into raving fans by helping them achieve their own business goals and aspirations through assisting them in raising their own innovation and marketing standards.

We provide our personalised and state-of-the-art services to our clients and boards who represent some of the world greatest innovative thinkers.
Updates

Here is some other information which may help shape your thinking.

I've had direct Involvement in the development of the following iPad, iPhone Applications and websites

FarbeyondOzlands.com (TerraLink platform) by Voyage Bureau
http://farbeyondozlands.example.au

Sail Verve by Bright Voyaging
https://apps.example-store.com/au/app/sail-verve/id100000001

uRedlandTR by Travel Territory Board
https://apps.example-store.com/au/app/uredlandtr/id100000002

Wexmoor Trips
http://www.wexmoortrips.example.au

Trek Mapper by Voyage Bureau
http://apps.example-store.com/au/app/trek-mapper/id100000003

Sunward by Sunward Travel Office
https://apps.example-store.com/au/app/sunward/id100000004

Upper Fernridge Valley Route by Visit Coastlands
https://apps.example-store.com/au/app/upper-fernridge-valley-route/id100000005

Wanderer Path by Travel Territory Board and Southern Plains Travel Council
https://apps.example-store.com/au/app/wanderers-path-grand-journey/id100000006

Gordon Pellbrook Consulting (GPC)
November 2012 – Present (8 months)Brisbane, Sydney, Canberra

Gordon’s consults to Small-to-Medium Enterprises (SME) and Government organisations on business strategy, technology strategy, risk mitigation, disruptive technology and innovation in the workplace.

Gordon’s consultancy mantra is that we cannot divorce economic life from cultural life particularly in an era when social capital may be as important as physical capital in business.

Reason: request from designers, I want to see their best efforts

Target Market(s)

35+

Industry/Entity Type

Business

Requirements
Must have
• Please use some of the personal image(s) contained in the zip files which can be downloaded from here

http://filedrop.example/k9Xq2Lm
http://filedrop.example/p4Rt7Vn
http://filedrop.example/z8Hw3Bc
Nice to have
• Black, Sleek design, maybe minimalist. Nice to have a Pixelle for the design. Nice to have it easily ported to Wordpress or be a modified Wordpress template. HTML 5, responsive design

```html
<!DOCTYPE html>
<html lang="en">
<head>
<meta charset="utf-8">
<title>Gordon Pellbrook Consulting</title>
<link href="https://fonts.googleapis.com/css2?family=Cinzel:wght@400;700&family=Ubuntu:wght@400;500&family=Arimo:wght@400;700&display=swap" rel="stylesheet">
<style>
:root{
  --bg:#1c1c1c;
  --bg-dark:#161616;
  --header:#1e1e1e;
  --nav:#2c2c2c;
  --nav-active:#1d1d1d;
  --line:#4a4a4a;
  --text:#c9c9c9;
  --muted:#8a8a8a;
  --white:#ffffff;
  --accent:#9fb6cc;
  --card:#121212;
  --footer:#2a2a2a;
}
*{margin:0;padding:0;box-sizing:border-box}
html,body{width:1124px;height:1200px;overflow:hidden;background:var(--bg);font-family:"Arimo",Arial,sans-serif;color:var(--text)}
.page{position:relative;width:1124px;height:1200px;background:var(--bg)}
.site-header{height:97px;background:linear-gradient(#242424,#1a1a1a);text-align:center;padding-top:14px}
.brand-name{font-family:"Cinzel",serif;font-weight:700;font-size:34px;color:var(--white);letter-spacing:.5px;line-height:38px}
.brand-sub{display:flex;align-items:center;gap:14px;margin:2px 84px 0}
.brand-sub::before,.brand-sub::after{content:"";flex:1;height:1px;background:var(--line)}
.brand-sub span{font-family:"Cinzel",serif;font-size:25px;color:#d6d6d6;letter-spacing:1px}
.main-nav{height:53px;background:linear-gradient(#333,#262626);border-top:1px solid #3a3a3a;border-bottom:1px solid #111}
.main-nav .inner{margin:0 84px;display:flex;height:100%;align-items:stretch}
.nav-item{display:flex;align-items:center;padding:0 21px;font-family:"Ubuntu",sans-serif;font-size:13px;color:#bdbdbd;border-left:1px solid #1a1a1a;border-right:1px solid #3b3b3b;text-transform:uppercase}
.nav-item.active{background:var(--nav-active);color:var(--white);padding:0 25px}
.call{margin-left:auto;display:flex;align-items:center;gap:10px;font-family:"Ubuntu",sans-serif;font-size:19px;color:#bbb}
.call b{font-weight:500;color:#d0d0d0}
.hero{position:absolute;left:84px;top:174px;width:956px;height:366px;border:1px solid #3b5269;background:radial-gradient(ellipse at 80% 30%,#7fa5c8 0%,#4b6d8e 35%,#253a50 70%,#1b2a3a 100%);box-shadow:0 8px 14px rgba(0,0,0,.6)}
.hero h1{position:absolute;left:27px;top:88px;font-family:"Ubuntu",sans-serif;font-weight:500;font-size:25px;line-height:40px;color:#b8cbe0}
.btn{position:absolute;left:27px;top:176px;width:164px;height:49px;border-radius:3px;background:linear-gradient(#a9c0dc,#7e9bbd);font-family:"Ubuntu",sans-serif;font-weight:500;font-size:20px;color:#1d2836;display:flex;align-items:center;justify-content:center}
.portrait{position:absolute;right:0;top:0;width:360px;height:364px;background:linear-gradient(#8fb0cf,#6f93b8)}
.arrows{position:absolute;left:27px;top:326px;display:flex;gap:6px}
.welcome{position:absolute;left:84px;top:588px;width:700px}
.welcome h2{font-family:"Ubuntu",sans-serif;font-weight:400;font-size:22px;color:var(--accent);margin-bottom:14px}
.welcome p{font-size:13px;line-height:21.5px;color:#c4c4c4;text-align:justify}
.welcome-photo{position:absolute;left:811px;top:592px;width:230px;height:142px;border:1px solid #333;background:#0e0e0e;padding:6px}
.welcome-photo div{width:100%;height:100%;background:linear-gradient(#7f90c4,#a7b3d8)}
.divider{position:absolute;left:84px;top:765px;width:956px;height:2px;background:#0c0c0c;border-bottom:1px solid #333}
.cards{position:absolute;left:84px;top:788px;display:flex;gap:25px}
.card{width:227px;height:283px;background:var(--card);border:1px solid #2b2b2b;padding:6px}
.card .thumb{height:124px}
.card h3{font-family:"Ubuntu",sans-serif;font-weight:400;font-size:17px;color:#d8d8d8;margin:16px 0 12px 11px}
.card p{font-size:13px;line-height:21.5px;color:var(--muted);margin:0 11px;text-align:justify}
.card a{display:block;margin:8px 11px 0;font-size:13px;color:#d0d0d0;text-decoration:none}
.site-footer{position:absolute;left:0;top:1100px;width:1124px;height:100px;background:var(--footer);border-top:1px solid #3a3a3a}
.footer-nav{position:absolute;left:83px;top:24px;font-size:13px;font-weight:700;color:#aaa}
.footer-nav .current{color:var(--white)}
.footer-nav i{font-style:normal;margin:0 9px;color:#aaa}
.copyright{position:absolute;left:83px;top:57px;font-size:13px;font-weight:700;color:#aaa;word-spacing:2px}
.social{position:absolute;right:84px;top:36px;display:flex;gap:10px;font-size:12px;font-weight:700;color:#c8c8c8}
</style>
</head>
<body>
<div class="page">
  <header class="site-header">
    <div class="brand-name">GORDON PELLBROOK</div>
    <div class="brand-sub"><span>CONSULTING</span></div>
  </header>
  <nav class="main-nav">
    <div class="inner">
      <div class="nav-item active">Home</div>
      <div class="nav-item">About Me</div>
      <div class="nav-item">Our Services</div>
      <div class="nav-item">Resources</div>
      <div class="nav-item">Clients</div>
      <div class="nav-item">Contact Us</div>
      <div class="call">
        <svg width="18" height="18" viewBox="0 0 24 24"><path d="M6.6 10.8c1.4 2.8 3.8 5.1 6.6 6.6l2.2-2.2c.3-.3.7-.4 1-.2 1.1.4 2.3.6 3.6.6.6 0 1 .4 1 1V20c0 .6-.4 1-1 1C10.6 21 3 13.4 3 4c0-.6.4-1 1-1h3.5c.6 0 1 .4 1 1 0 1.3.2 2.5.6 3.6.1.3 0 .7-.2 1z" fill="#999"/></svg>
        <span>CALL US : <b>555 210 4873</b></span>
      </div>
    </div>
  </nav>

  <section class="hero">
    <h1>I do Edgy Consulting Business Specializing<br>in innovation, technology and strategy.</h1>
    <div class="btn">CONTACT ME</div>
    <div class="portrait" role="img" aria-label="Portrait photo of the consultant in a light grey blazer"></div>
    <div class="arrows">
      <svg width="25" height="25" viewBox="0 0 25 25"><circle cx="12.5" cy="12.5" r="12" fill="#555"/><path d="M14.5 7.5l-5 5 5 5" stroke="#ddd" stroke-width="2.5" fill="none"/></svg>
      <svg width="25" height="25" viewBox="0 0 25 25"><circle cx="12.5" cy="12.5" r="12" fill="#555"/><path d="M10.5 7.5l5 5-5 5" stroke="#ddd" stroke-width="2.5" fill="none"/></svg>
    </div>
  </section>

  <section class="welcome">
    <h2>Welcome to our site</h2>
    <p>Fusce at quam at turpis luctus bibendum. Duis condimentum risus metus, eget posuere augue adipiscing in. Cras tincidunt leo nulla, nec molestie sapien porttitor ut. Curabitur ac nulla erat. Nullam non augue eget arcu volutpat pretium feugiat sit amet dui. Suspendisse lacinia felis eleifend magna mattis, nec vestibulum neque viverra. In tincidunt est massa, ut viverra ante congue et. Nam imperdiet dignissim pharetra. Proin vestibulum sed magna eu suscipit. Ut pharetra mi vel cursus pharetra. Morbi viverra nisl ut mauris vulputate facilisis. In faucibus dignissim leo</p>
  </section>
  <div class="welcome-photo"><div role="img" aria-label="Photo of a businessman breaking through a finish line ribbon against a blue sky"></div></div>

  <div class="divider"></div>

  <section class="cards">
    <article class="card">
      <div class="thumb" role="img" aria-label="Black and white photo of a hand moving chess pieces" style="background:radial-gradient(circle at 50% 40%,#e8e8e8,#777 60%,#222)"></div>
      <h3>Strategies</h3>
      <p>Duis condimentum risus metus, eget posuere auguela adipiscing in. Cras tincidunt leo nulla,</p>
      <a href="#">View more</a>
    </article>
    <article class="card">
      <div class="thumb" role="img" aria-label="Monochrome photo of a rising bar chart" style="background:linear-gradient(135deg,#111,#555 60%,#999)"></div>
      <h3>Productivity</h3>
      <p>Duis condimentum risus metus, eget posuere auguela adipiscing in. Cras tincidunt leo nulla,</p>
      <a href="#">View more</a>
    </article>
    <article class="card">
      <div class="thumb" role="img" aria-label="Black and white illustration of hands holding gears" style="background:linear-gradient(#ddd,#777)"></div>
      <h3>Solutions</h3>
      <p>Duis condimentum risus metus, eget posuere auguela adipiscing in. Cras tincidunt leo nulla,</p>
      <a href="#">View more</a>
    </article>
    <article class="card">
      <div class="thumb" role="img" aria-label="Black and white photo of stacked team hands" style="background:linear-gradient(135deg,#333,#aaa 50%,#444)"></div>
      <h3>Support</h3>
      <p>Duis condimentum risus metus, eget posuere auguela adipiscing in. Cras tincidunt leo nulla,</p>
      <a href="#">View more</a>
    </article>
  </section>

  <footer class="site-footer">
    <div class="footer-nav"><span class="current">Home</span><i>|</i>About Me<i>|</i>Our Services<i>|</i>Resources<i>|</i>Clients<i>|</i>Contact us</div>
    <div class="copyright">Copyright © 2013 &nbsp;Gordon Pellbrook consulting. &nbsp;&nbsp;All rights reserved.</div>
    <div class="social"><span>Friendbook</span><span>Chirper</span></div>
  </footer>
</div>
</body>
</html>
```